Harbor Crest Residential Business Card Design - Logo Provided

business card design - LOGO PROVIDED. private capital fund investing in: commercial real estate (apartments), asset backed lending, private credit, flexible capital

Target Market(s)

private capital: commercial real estate (apartments), asset backed lending, private credit, flexible capital

Industry/Entity Type

alternative asset management

Contact Information for Business Card

logo, name, title, phone number, email and website

Font styles to use
Sans Serif

Colors
0054AA
0677BA
7BADD7
CADEEF
E8F1F8
EB3D1F
EC4F4E
F09395
F8D3D4
FCEDEE

Requirements
Must have
• use of logo on both sides and a qr code on the back

```html
<!DOCTYPE html>
<html lang="en">
<head>
<meta charset="utf-8">
<title>Harbor Crest Residential – Business Card</title>
<link rel="stylesheet" href="https://fonts.googleapis.com/css2?family=Lato:ital,wght@0,400;0,700;0,900;1,900&display=swap">
<style>
  :root {
    --stage: #151515;
    --card-red: #e02128;
    --card-light: #e7e6e8;
    --white: #ffffff;
    --brand-red: #e3232b;
    --navy: #1f2d6b;
    --ink: #1b1b1b;
  }
  * { margin: 0; padding: 0; box-sizing: border-box; }
  html, body {
    width: 1200px; height: 1000px; overflow: hidden;
    background: var(--stage);
    font-family: "Lato", Arial, sans-serif;
  }
  .canvas { position: relative; width: 1200px; height: 1000px; }

  .card {
    position: absolute; left: 220px; width: 761px; height: 435px;
    border-radius: 30px; overflow: hidden;
  }
  .card--front { top: 50px; background: var(--card-red); }
  .card--back  { top: 515px; height: 434px; background: var(--card-light); }

  /* front */
  .front-mark {
    position: absolute; left: 360px; top: 128px; width: 160px;
    display: flex; align-items: center; gap: 10px;
  }
  .front-mark__square { width: 22px; height: 22px; background: var(--white); flex: none; }
  .front-mark__name {
    color: var(--white); font-weight: 900; font-size: 25px; line-height: 1.05;
    text-transform: uppercase;
  }
  .front-banner {
    position: absolute; left: 185px; top: 277px; width: 506px; height: 59px;
    border-top: 1.5px solid var(--white); border-bottom: 1.5px solid var(--white);
    display: flex; align-items: center; justify-content: center;
  }
  .front-banner__text {
    color: var(--white); font-weight: 900; font-size: 27px; letter-spacing: 0.5px;
    text-transform: uppercase;
  }

  /* back */
  .person { position: absolute; left: 54px; top: 72px; }
  .person__name {
    color: var(--brand-red); font-weight: 900; font-size: 35px; line-height: 1;
    text-transform: uppercase; letter-spacing: -0.3px;
  }
  .person__title { color: var(--ink); font-size: 17px; margin-top: 6px; }

  .contact { position: absolute; left: 56px; top: 183px; list-style: none; }
  .contact__item {
    display: flex; align-items: center; gap: 8px;
    color: var(--ink); font-weight: 700; font-size: 20px; height: 36.5px;
  }
  .contact__icon { width: 20px; height: 20px; flex: none; }

  .back-mark {
    position: absolute; left: 505px; top: 176px; width: 170px;
    display: flex; align-items: center; gap: 10px;
  }
  .back-mark__square { width: 22px; height: 22px; background: var(--navy); flex: none; }
  .back-mark__name {
    color: var(--navy); font-weight: 900; font-size: 24px; line-height: 1.05;
    text-transform: uppercase;
  }

  .address {
    position: absolute; left: 0; right: 0; top: 353px;
    text-align: center; color: var(--ink); font-size: 15px;
  }
</style>
</head>
<body>
<main class="canvas">

  <section class="card card--front" aria-label="Card front">
    <div class="front-mark">
      <span class="front-mark__square"></span>
      <span class="front-mark__name">Harbor Crest Residential</span>
    </div>
    <div class="front-banner">
      <span class="front-banner__text">Harbor Crest Residential</span>
    </div>
  </section>

  <section class="card card--back" aria-label="Card back">
    <div class="person">
      <h1 class="person__name">Laura Bennett</h1>
      <p class="person__title">Managing Director</p>
    </div>

    <ul class="contact">
      <li class="contact__item">
        <svg class="contact__icon" viewBox="0 0 24 24" aria-hidden="true">
          <path fill="var(--navy)" d="M6.6 10.8a15.1 15.1 0 0 0 6.6 6.6l2.2-2.2c.3-.3.7-.4 1-.2 1.1.4 2.3.6 3.6.6.6 0 1 .4 1 1V20c0 .6-.4 1-1 1A17 17 0 0 1 3 4c0-.6.4-1 1-1h3.5c.6 0 1 .4 1 1 0 1.3.2 2.5.6 3.6.1.3 0 .7-.2 1z"/>
        </svg>
        044-987 654 321
      </li>
      <li class="contact__item">
        <svg class="contact__icon" viewBox="0 0 24 24" aria-hidden="true">
          <rect x="2" y="5" width="20" height="14" rx="1.5" fill="var(--navy)"/>
          <path d="M3 6l9 7 9-7" fill="none" stroke="var(--card-light)" stroke-width="1.6"/>
        </svg>
        info@harborcrest.com
      </li>
      <li class="contact__item">
        <svg class="contact__icon" viewBox="0 0 24 24" aria-hidden="true">
          <g fill="none" stroke="var(--navy)" stroke-width="1.8">
            <circle cx="12" cy="12" r="9"/>
            <ellipse cx="12" cy="12" rx="4" ry="9"/>
            <path d="M3 12h18M4.5 7.5h15M4.5 16.5h15"/>
          </g>
        </svg>
        www.harborcrest.com
      </li>
    </ul>

    <div class="back-mark">
      <span class="back-mark__square"></span>
      <span class="back-mark__name">Harbor Crest Residential</span>
    </div>

    <p class="address">412 Harbor View Rd Bayport, FL 33500, 2250 Coastal Way Port Lane, FL 33900</p>
  </section>

</main>
</body>
</html>
```